Book Cover for Herb Growing and Ancient Medecine Recipes for People over 50 years

The front book cover shall
- be an eye-catcher even as small as a thumbnail on a cell phone
- contain the following words:
Title: The Patient Beekeeper
Subtitle: Our detours to Coastal Lanterns
Hook: Effortless fixes for:
• Sleep like never before
• Pain-free movement
• Hair that thrives
• Calm hormones
Author name: Lionel Dravec
- meet Velmora QTL print requirements for size, CMYK colors etc.

Attached are covers of best-selling book in my genre.

Target Market(s)

Velmora book buyers over 50 yrs with some health issues who want to improve their well-being naturally

Colors
00AB8E
00BBA5
67D7C9
C6EFE9
E9F9F6

Requirements
Must have
• a catchy main image

```html
<!DOCTYPE html>
<html lang="en">
<head>
<meta charset="utf-8">
<title>The Patient Beekeeper — Book Cover</title>
<link rel="stylesheet" href="https://fonts.googleapis.com/css2?family=Big+Shoulders+Inline+Display:wght@700&family=Great+Vibes&family=Josefin+Sans:wght@600&family=Archivo:wght@400;700&display=swap">
<style>
  :root {
    --stage: #000000;
    --paper: #ddceb0;
    --ink-green: #173d3a;
    --ink-brown: #3a221e;
    --ink-dark: #2e2220;
    --band-text: #ddceae;
    --art-light: #d3c3a2;
    --art-mid: #b7b09a;
  }
  * { margin: 0; padding: 0; box-sizing: border-box; }
  html, body {
    width: 976px; height: 1200px; overflow: hidden;
    background: var(--stage);
  }
  .stage {
    position: relative; width: 976px; height: 1200px;
    background: var(--stage);
  }
  .cover {
    position: absolute; left: 183px; top: 168px;
    width: 610px; height: 864px;
    background: var(--paper);
  }
  .title-article {
    position: absolute; left: 0; right: 0; top: 40px;
    text-align: center;
    font-family: "Great Vibes", cursive;
    font-size: 64px; line-height: 1;
    color: var(--ink-green);
  }
  .title-line {
    position: absolute; left: 0; right: 0;
    text-align: center;
    font-family: "Big Shoulders Inline Display", sans-serif;
    font-weight: 700;
    color: var(--ink-green);
    line-height: 1;
    letter-spacing: 2px;
  }
  .title-line--first { top: 100px; font-size: 102px; }
  .title-line--second { top: 199px; font-size: 102px; }
  .subtitle {
    position: absolute; left: 0; right: 0; top: 313px;
    text-align: center;
    font-family: "Josefin Sans", sans-serif;
    font-weight: 600;
    font-size: 19px;
    text-transform: uppercase;
    color: var(--ink-brown);
  }
  .main-art {
    position: absolute; left: 136px; top: 352px;
    width: 275px; height: 300px;
    background: radial-gradient(ellipse at 50% 55%, var(--art-mid) 0%, var(--art-light) 55%, var(--paper) 80%);
    border-radius: 8px;
  }
  .hook {
    position: absolute; left: 81px; width: 444px; top: 675px;
    display: flex; align-items: center; gap: 14px;
    font-family: "Archivo", sans-serif;
    font-size: 14px; color: var(--ink-dark);
    text-transform: uppercase; letter-spacing: 0.3px;
    white-space: nowrap;
  }
  .hook__rule { flex: 1; height: 1px; background: var(--ink-dark); }
  .benefits {
    position: absolute; left: 75px; width: 457px; top: 702px;
    display: flex;
    list-style: none;
    font-family: "Archivo", sans-serif;
    font-size: 14.5px; line-height: 19px;
    color: var(--ink-dark);
    text-transform: uppercase;
    text-align: center;
  }
  .benefits li {
    padding: 2px 0;
    border-left: 1px solid var(--ink-dark);
  }
  .benefits li:first-child { border-left: none; width: 126px; }
  .benefits li:nth-child(2) { width: 115px; }
  .benefits li:nth-child(3) { width: 105px; }
  .benefits li:nth-child(4) { width: 111px; }
  .author-band {
    position: absolute; left: 76px; top: 759px;
    width: 455px; height: 54px;
    background: var(--ink-green);
    display: flex; align-items: center; justify-content: center;
    font-family: "Archivo", sans-serif;
    font-weight: 700; font-size: 24px;
    letter-spacing: 0.5px;
    color: var(--band-text);
    text-transform: uppercase;
  }
</style>
</head>
<body>
  <main class="stage">
    <section class="cover">
      <h1>
        <span class="title-article">The</span>
        <span class="title-line title-line--first">PATIENT</span>
        <span class="title-line title-line--second">BEEKEEPER</span>
      </h1>
      <p class="subtitle">Our detours to Coastal Lanterns</p>
      <div class="main-art" role="img" aria-label="Engraved line drawing of a mortar and pestle filled with herbs and flowers, with a daisy and seeds beside it"></div>
      <p class="hook"><span class="hook__rule"></span>Effortless fixes for<span class="hook__rule"></span></p>
      <ul class="benefits">
        <li>Sleep like<br>never before</li>
        <li>Pain-free<br>movement</li>
        <li>Hair that<br>thrives</li>
        <li>Calm<br>hormones</li>
      </ul>
      <p class="author-band">Lionel Dravec</p>
    </section>
  </main>
</body>
</html>
```